Graphic Banner Design - 2.5' x 6' - High Tech Company

We are in need of a banner design for an outdoor sign that will be used at sponsorship events.

Size
2.5' x 6'

The company is a high tech company, and the design will be used for action sports events. So lining up to that would be good.

Tag line to be incorporated...
"Extreme IT Services for Extreme Needs."

Target Market(s)

Business Owners, Entrepreneurs, IT Professionals.

Industry/Entity Type

Information Technology

Logo Text

Vexlora

Colors

Designer to choose colors to be used in the design.

Requirements
Must have
• Must feel young and vibrant, fit in to an action sports event and just be out of this world awesome.
• In the world of the IT, we are the Zanverolli. Fast, Awesome, not necessarily cheap, but you know it will do what you want extremely well. Not for everyone, but always desired.

```html
<!DOCTYPE html>
<html lang="en">
<head>
<meta charset="utf-8">
<title>Vexlora – Event Banner</title>
<link href="https://fonts.googleapis.com/css2?family=Jost:wght@400;500&family=Montserrat:wght@500&display=swap" rel="stylesheet">
<style>
  :root {
    --page-bg: #ffffff;
    --banner-deep: #1d1f4a;
    --banner-violet: #6a5bc4;
    --banner-cyan: #6fd3e0;
    --banner-magenta: #d86ad0;
    --banner-mint: #5ee8c0;
    --flare: #f4eeff;
    --headline: #ffffff;
    --logo-ink: #111111;
    --caption: #6e6e6e;
  }
  * { margin: 0; padding: 0; box-sizing: border-box; }
  html, body {
    width: 1200px; height: 1000px; overflow: hidden;
    background: var(--page-bg);
  }
  .canvas { position: relative; width: 1200px; height: 1000px; }
  .banner {
    position: absolute; left: 90px; top: 248px;
    width: 1030px; height: 429px; overflow: hidden;
  }
  .banner-photo {
    position: absolute; inset: 0;
    background:
      radial-gradient(ellipse 260px 80px at 500px 40px, var(--flare) 0%, rgba(244,238,255,0.6) 35%, rgba(244,238,255,0) 100%),
      radial-gradient(ellipse 180px 260px at 960px 120px, rgba(216,106,208,0.55), rgba(216,106,208,0) 100%),
      radial-gradient(ellipse 160px 120px at 40px 30px, rgba(94,232,192,0.55), rgba(94,232,192,0) 100%),
      radial-gradient(ellipse 200px 260px at 1000px 380px, rgba(94,232,192,0.35), rgba(94,232,192,0) 100%),
      linear-gradient(180deg, var(--banner-violet) 0%, #4c5fb0 35%, #3a3f86 65%, var(--banner-deep) 100%);
  }
  .brand {
    position: absolute; top: 28px; left: 0; right: 0;
    display: flex; flex-direction: column; align-items: center; gap: 12px;
  }
  .brand-dot {
    width: 12px; height: 12px; border-radius: 50%;
    background: var(--logo-ink);
  }
  .brand-name {
    font-family: "Montserrat", sans-serif; font-weight: 500;
    font-size: 18px; color: var(--logo-ink); letter-spacing: 0.2px;
  }
  .headline {
    position: absolute; left: 52px; top: 166px;
    font-family: "Jost", sans-serif; font-weight: 400;
    font-size: 70px; line-height: 74px; color: var(--headline);
    text-transform: uppercase; letter-spacing: 0.5px;
  }
  .caption {
    position: absolute; left: 0; width: 1260px; top: 790px;
    text-align: center;
    font-family: "Jost", sans-serif; font-weight: 500;
    font-size: 28px; letter-spacing: 3.5px; color: var(--caption);
  }
</style>
</head>
<body>
<div class="canvas">
  <section class="banner">
    <div class="banner-photo" role="img" aria-label="Concert crowd under bright stage lights with neon shard effects and a dotted world map overlay"></div>
    <div class="brand">
      <span class="brand-dot"></span>
      <span class="brand-name">Vexlora</span>
    </div>
    <h1 class="headline">Extreme<br>IT Services<br>for Extreme Needs</h1>
  </section>
  <p class="caption">DRAFT DESIGN</p>
</div>
</body>
</html>
```